Business Card Design

we pay more for your estate jewelry .

Industry/Entity Type

Jewelry

Contact Information for Business Card

ray's coin and bullion llc .we buy gold , silver ,coins and diamonds.742 willow creek road Linden Heights nj 08099. 856-555-0148. open 7 days 9 to 7

```html
<!DOCTYPE html>
<html lang="en">
<head>
<meta charset="UTF-8">
<title>Ray's Coin and Bullion — Business Card</title>
<link href="https://fonts.googleapis.com/css2?family=Cinzel:wght@400;500&family=Questrial&display=swap" rel="stylesheet">
<style>
  :root {
    --backdrop: #1b1a19;
    --card: #2c2822;
    --gold: #d8b24a;
    --gold-soft: #b8923a;
  }
  html, body {
    margin: 0;
    width: 1200px;
    height: 900px;
    overflow: hidden;
    background: var(--backdrop);
  }
  .canvas {
    position: relative;
    width: 1200px;
    height: 900px;
    display: flex;
    align-items: center;
    justify-content: center;
  }
  .card {
    position: relative;
    width: 1000px;
    height: 572px;
    background: var(--card);
    box-shadow: 0 18px 40px rgba(0,0,0,.55);
    color: var(--gold);
  }
  .card-frame {
    position: absolute;
    inset: 0;
  }
  .flourish {
    position: absolute;
    background: linear-gradient(135deg, var(--gold), var(--gold-soft));
    opacity: .85;
    border-radius: 14px;
  }
  .flourish--tl { left: 40px; top: 40px; width: 80px; height: 34px; }
  .flourish--tr { right: 40px; top: 40px; width: 80px; height: 34px; }
  .flourish--bl { left: 40px; bottom: 40px; width: 80px; height: 34px; }
  .flourish--br { right: 40px; bottom: 40px; width: 80px; height: 34px; }
  .flourish--divider { left: 440px; top: 243px; width: 120px; height: 22px; }
  .brand {
    position: absolute;
    left: 150px;
    top: 118px;
    margin: 0;
    font-family: "Cinzel", serif;
    font-weight: 500;
    font-size: 56px;
    letter-spacing: 1px;
    white-space: nowrap;
    color: var(--gold);
  }
  .tagline {
    position: absolute;
    left: 156px;
    top: 200px;
    margin: 0;
    font-family: "Questrial", sans-serif;
    font-size: 27px;
    white-space: nowrap;
    color: var(--gold);
  }
  .contact {
    position: absolute;
    left: 0;
    right: 0;
    top: 292px;
    margin: 0;
    text-align: center;
    font-family: "Questrial", sans-serif;
    font-size: 30px;
    line-height: 44px;
    font-style: normal;
    color: var(--gold);
  }
  .contact .hours { font-size: 27px; }
</style>
</head>
<body>
<main class="canvas">
  <section class="card">
    <svg class="card-frame" width="1000" height="572" viewBox="0 0 1000 572" aria-hidden="true">
      <g fill="none" stroke="var(--gold)" stroke-width="2.5">
        <line x1="130" y1="57" x2="870" y2="57"/>
        <line x1="130" y1="515" x2="870" y2="515"/>
        <line x1="57" y1="90" x2="57" y2="482"/>
        <line x1="943" y1="90" x2="943" y2="482"/>
        <line x1="150" y1="254" x2="430" y2="254"/>
        <line x1="570" y1="254" x2="850" y2="254"/>
      </g>
    </svg>
    <div class="flourish flourish--tl" role="img" aria-label="Gold scroll ornament, top left corner"></div>
    <div class="flourish flourish--tr" role="img" aria-label="Gold scroll ornament, top right corner"></div>
    <div class="flourish flourish--bl" role="img" aria-label="Gold scroll ornament, bottom left corner"></div>
    <div class="flourish flourish--br" role="img" aria-label="Gold scroll ornament, bottom right corner"></div>
    <div class="flourish flourish--divider" role="img" aria-label="Gold scroll ornament on divider line"></div>

    <h1 class="brand">Ray's Coin and Bullion</h1>
    <p class="tagline">We buy Gold, Silver, Coins and Diamonds</p>
    <address class="contact">
      856-555-0148<br>
      742 Willow Creek Road Linden Heights<br>
      NJ 08099<br>
      <span class="hours">Open 7 days: 9 to 7</span>
    </address>
  </section>
</main>
</body>
</html>
```